Outdoor group fitness training - Greta Pollock Personal Training

I want an eye catching A4 flyer that promotes my two outdoor fitness groups. I have uploaded photos of each location: Brenton and Kilvane.
The target group is existing and potential new Personal training clients - all adults. There are two morning groups at Brenton ; one evening and one morning group at Kilvane. The groups will be for up to 8 people and are for all fitness levels.I want to encourage people to come and have a go. I have also uploaded a design I have used through inkrally for a previous flyer. I would like to use the orange graphic of the two people at the bottom of this design.
Cost is $15 per person
Location and times - Brenton Green Wednesdays 7.30am; Sundays 8am
Kilvane High School Thursdays 6.30pm: Saturdays 8am
Updates

Thanks so much to all of you for submitting a great set of designs. it was really hard making a choice in the end, and I really appreciate the promptness and creativity that went into the designs. I will certainly keep you in mind for future jobs. Cheers and have a great day Greta Pollock

Target Market(s)

40 - 60 year old adults: cross section of professionals, tradespeople and retirees. People who will enjoy socialising while also getting fit. No extremely fit people - cross section of beginners to intermediate; males and females

Industry/Entity Type

Training

Font styles to use
Sans Serif

Colors
f78f20
9bcb3c
ecf7fb

Requirements
Must have
• Fast turnaround required - within two days
Bright and attention grabbing, engaging. Could be A4 or could be postcard size?

State cost clearly
State that first 5 people to join either group will get first session at half price

```html
<!DOCTYPE html>
<html lang="en">
<head>
<meta charset="utf-8">
<title>Greta Pollock Personal Training – Outdoor Group Fitness</title>
<link href="https://fonts.googleapis.com/css2?family=Source+Sans+3:wght@300;400;600;700&display=swap" rel="stylesheet">
<style>
  :root {
    --orange: #f78f20;
    --green: #9bcb3c;
    --white: #ffffff;
    --ink: #333333;
    --sepia-dark: #6b4a33;
    --sepia-mid: #a88466;
    --sepia-light: #d9c2a8;
    --park-green: #6f8f4a;
    --park-sky: #cfe0ea;
  }
  * { box-sizing: border-box; margin: 0; padding: 0; }
  html, body { width: 849px; height: 1200px; overflow: hidden; background: var(--white); }
  body { font-family: "Source Sans 3", Arial, sans-serif; }

  .flyer { position: relative; width: 849px; height: 1200px; overflow: hidden; background: var(--white); }

  /* Header */
  .header-band { position: absolute; left: 0; top: 0; }
  .brand { position: absolute; left: 436px; top: 38px; display: flex; align-items: center; gap: 28px; }
  .brand-name { color: var(--orange); font-size: 36px; font-weight: 700; letter-spacing: -0.3px; }
  .brand-dot { width: 58px; height: 58px; border-radius: 50%; background: var(--orange); margin-left: 70px; }

  /* Hero */
  .hero { position: absolute; left: 0; top: 121px; width: 849px; height: 389px;
    background: linear-gradient(100deg, var(--sepia-dark) 0%, var(--sepia-mid) 45%, var(--sepia-light) 100%); }
  .hero-title-band { position: absolute; left: 0; bottom: 0; width: 100%; height: 105px;
    background: linear-gradient(90deg, rgba(255,255,255,0) 0%, rgba(255,255,255,0.25) 100%); }
  .hero-title { position: absolute; right: 28px; bottom: 20px; color: var(--white);
    font-size: 64px; font-weight: 300; text-shadow: 0 2px 4px rgba(0,0,0,0.35); }
  .price-badge { position: absolute; left: -10px; top: 118px; }

  /* Benefits */
  .benefits { position: absolute; left: 30px; top: 534px; list-style: none; }
  .benefits li { display: flex; align-items: center; height: 54.5px; color: var(--orange);
    font-size: 23px; font-weight: 600; }
  .benefits svg { margin-right: 22px; flex: none; }

  /* Venues */
  .venue { position: absolute; top: 816px; height: 242px; width: 421px; }
  .venue-brenton { left: 0; background: linear-gradient(180deg, var(--park-sky) 0%, #8aa86a 45%, var(--park-green) 100%); }
  .venue-kilvane { left: 428px; background: linear-gradient(180deg, #9fb98a 0%, #b7c3a8 45%, #a9a9a2 100%); }
  .venue-caption { position: absolute; left: 0; bottom: 0; width: 100%; height: 44px;
    background: rgba(60,60,60,0.55); color: var(--white); font-size: 16.5px; padding: 11px 26px; }
  .venue-kilvane .venue-caption { text-align: right; padding-right: 12px; }

  /* Footer */
  .footer-band { position: absolute; left: 0; top: 1094px; }
  .footer-cost { position: absolute; left: 27px; top: 1112px; color: var(--orange); font-size: 21px; font-weight: 700; }
  .footer-label { position: absolute; left: 27px; top: 1148px; color: var(--orange); font-size: 20px; font-weight: 400; }
  .schedule { position: absolute; right: 18px; top: 1109px; text-align: right; color: var(--white);
    font-size: 21px; font-weight: 600; line-height: 36px; }
</style>
</head>
<body>
<main class="flyer">

  <svg class="header-band" width="849" height="121" aria-hidden="true">
    <polygon points="0,0 460,0 390,118 0,118" fill="var(--green)"/>
  </svg>
  <div class="brand">
    <span class="brand-name">Greta Pollock</span>
    <span class="brand-dot" aria-hidden="true"></span>
  </div>

  <section class="hero" role="img" aria-label="Photo of two people jogging along a waterfront path, warm sepia tones">
    <div class="hero-title-band"></div>
    <h1 class="hero-title">Why Join Us</h1>
  </section>

  <svg class="price-badge" width="180" height="200" viewBox="0 0 180 200" aria-label="$15 per person">
    <polygon fill="var(--green)" points="85,0 100,48 145,22 130,70 178,72 138,100 178,128 130,130 145,178 100,152 85,200 72,152 26,178 42,130 -6,128 32,100 -6,72 42,70 26,22 72,48"/>
    <circle cx="85" cy="100" r="70" fill="var(--white)"/>
    <circle cx="85" cy="100" r="64" fill="var(--orange)"/>
    <text x="85" y="107" text-anchor="middle" fill="var(--white)" font-family="Source Sans 3, Arial, sans-serif" font-size="52" font-weight="700" font-style="italic">$15</text>
    <text x="85" y="140" text-anchor="middle" fill="var(--white)" font-family="Source Sans 3, Arial, sans-serif" font-size="26" font-weight="700" font-style="italic">p/p</text>
  </svg>

  <ul class="benefits">
    <li><svg width="26" height="26" viewBox="0 0 26 26" aria-hidden="true"><polygon fill="var(--green)" points="13,0 15.5,8 23,3 18,10.5 26,13 18,15.5 23,23 15.5,18 13,26 10.5,18 3,23 8,15.5 0,13 8,10.5 3,3 10.5,8"/></svg>First 5 people to join either group will get first session at half price</li>
    <li><svg width="26" height="26" viewBox="0 0 26 26" aria-hidden="true"><polygon fill="var(--green)" points="13,0 15.5,8 23,3 18,10.5 26,13 18,15.5 23,23 15.5,18 13,26 10.5,18 3,23 8,15.5 0,13 8,10.5 3,3 10.5,8"/></svg>8 People per group</li>
    <li><svg width="26" height="26" viewBox="0 0 26 26" aria-hidden="true"><polygon fill="var(--green)" points="13,0 15.5,8 23,3 18,10.5 26,13 18,15.5 23,23 15.5,18 13,26 10.5,18 3,23 8,15.5 0,13 8,10.5 3,3 10.5,8"/></svg>Suitable for all fitness levels</li>
    <li><svg width="26" height="26" viewBox="0 0 26 26" aria-hidden="true"><polygon fill="var(--green)" points="13,0 15.5,8 23,3 18,10.5 26,13 18,15.5 23,23 15.5,18 13,26 10.5,18 3,23 8,15.5 0,13 8,10.5 3,3 10.5,8"/></svg>Two outdoor fitness groups (Brenton &amp; Kilvane)</li>
    <li><svg width="26" height="26" viewBox="0 0 26 26" aria-hidden="true"><polygon fill="var(--green)" points="13,0 15.5,8 23,3 18,10.5 26,13 18,15.5 23,23 15.5,18 13,26 10.5,18 3,23 8,15.5 0,13 8,10.5 3,3 10.5,8"/></svg>Great place to socilaise and excersise</li>
  </ul>

  <figure class="venue venue-brenton" role="img" aria-label="Photo of Brenton Green park with trees and lawn">
    <figcaption class="venue-caption">Brenton Green Wednesdays</figcaption>
  </figure>
  <figure class="venue venue-kilvane" role="img" aria-label="Photo of Kilvane High School oval and pavilion">
    <figcaption class="venue-caption">Kilvane High School Thursdays</figcaption>
  </figure>

  <svg class="footer-band" width="849" height="106" aria-hidden="true">
    <polygon points="310,0 849,0 849,106 212,106" fill="var(--green)"/>
  </svg>
  <p class="footer-cost">Cost is $15 per person</p>
  <p class="footer-label">Location and Timing</p>
  <div class="schedule">
    <p>Brenton Green - Wednesdays 7.30am &amp; Sundays 8am</p>
    <p>Kilvane High School - Thursdays 6.30pm: &amp; Saturdays 8am</p>
  </div>

</main>
</body>
</html>
```